Harrowgate Legal

To update and modernize current business card appearance. Marisa's business is based in Melbourne with 4 other lawyers in the firm. Marisa travels to the Pilbara in Western Australia approximately 1 week a month as part of the firms legal work. She consults with clients in Newman, Tom Price and Port Hedland. The lawyers work mostly from a home office, apart from court appearances. They have a virtual office in Melbourne city, and use facilities in 3 or 4 other locations around Melbourne. It is important the client's think this is a conventional law firm with a permanent office. Our business structure is a difficult concept for them to grasp. The business has been operational for 3 years, growing from 1 lawyer to 4 lawyers during that time. Our website is www.Harrowgatelegal.com.au and is currently being upgraded as we are not happy with its content. The logo is currently orange and dark grey but the orange is a difficult colour to reproduce and often turns out "poo" brown when documents are printed. We need clients to know we are user friendly and caring - and not head up our rears ends as some lawyers appear to be.
Updates

Thank you for the feedback so far. 1. Some of the designs have too much black (We prefer darker grey & not too much.) 2. Happy for designers to play around with different colours & logo design. What we're after is a modern look and business card that people say "wow" when they pick it up.

Industry/Entity Type

Business

```html
<!DOCTYPE html>
<html lang="en">
<head>
<meta charset="utf-8">
<title>Harrowgate Legal – Business Card</title>
<link rel="stylesheet" href="https://fonts.googleapis.com/css2?family=Cinzel:wght@400;600&family=Open+Sans:wght@400;600&display=swap">
<style>
  :root {
    --backdrop: #8b5e3c;
    --card: #ffffff;
    --brand-red: #ee3a2b;
    --ink: #333336;
    --soft-grey: #a9a9ab;
  }
  * { margin: 0; padding: 0; box-sizing: border-box; }
  html, body {
    width: 1200px; height: 480px; overflow: hidden;
    background: var(--backdrop);
  }
  .canvas { position: relative; width: 1200px; height: 480px; }
  .card {
    position: absolute;
    width: 473px; height: 270px;
    background: var(--card);
    overflow: hidden;
  }
  .card--front { left: 80px; top: 90px; }
  .card--back { left: 593px; top: 93px; }

  .brand {
    position: absolute;
    display: flex; align-items: center; gap: 12px;
    font-family: "Cinzel", serif;
    font-weight: 600;
    color: var(--ink);
    font-size: 23px;
    line-height: 1.15;
    letter-spacing: 0.5px;
  }
  .brand__dot {
    width: 30px; height: 30px; border-radius: 50%;
    background: var(--brand-red); flex: none;
  }
  .card--front .brand { left: 40px; top: 70px; }
  .card--back .brand { left: 50%; top: 82px; transform: translateX(-50%); }

  .holder-name {
    position: absolute; right: 30px; top: 36px;
    font-family: "Cinzel", serif; font-weight: 400;
    font-size: 18px; letter-spacing: 0.5px;
    color: var(--brand-red);
  }
  .contact {
    position: absolute; right: 30px; top: 120px;
    text-align: right;
    font-family: "Open Sans", sans-serif;
    font-size: 12px; line-height: 19px;
    color: var(--ink);
  }
  .contact__web { font-weight: 600; letter-spacing: 0.3px; }
  .contact__address { margin-top: 12px; line-height: 16px; }

  .swoosh { position: absolute; left: 0; top: 0; width: 473px; height: 270px; }

  .back-web {
    position: absolute; left: 0; right: 0; top: 208px;
    text-align: center;
    font-family: "Open Sans", sans-serif; font-weight: 600;
    font-size: 12px; letter-spacing: 0.8px;
    color: #4a4a4d;
  }
</style>
</head>
<body>
<main class="canvas">
  <section class="card card--front">
    <svg class="swoosh" viewBox="0 0 473 270" aria-hidden="true">
      <path d="M0 190 C150 214 320 232 473 233 L473 241 C320 240 150 224 0 200 Z" fill="var(--soft-grey)"/>
      <path d="M0 200 C150 224 320 240 473 241 L473 270 L0 270 Z" fill="var(--brand-red)"/>
    </svg>
    <div class="brand">
      <span class="brand__dot"></span>
      <span>Harrowgate<br>Legal</span>
    </div>
    <p class="holder-name">Your Name Here</p>
    <div class="contact">
      <p>Tel: 012.345.6789</p>
      <p>Email: info@harrowgate.com</p>
      <p class="contact__web">www.Harrowgatelegal.com.au</p>
      <p class="contact__address">Suite 000, Cityname<br>country name</p>
    </div>
  </section>

  <section class="card card--back">
    <div class="brand">
      <span class="brand__dot"></span>
      <span>Harrowgate<br>Legal</span>
    </div>
    <p class="back-web">www.Harrowgatelegal.com.au</p>
  </section>
</main>
</body>
</html>
```